Business Card and Stationary Design

After the successful redesign of our logo we are wanting to follow suite and create a new business card and stationary design!

New Logo is attached, information required on the business card should contain a mixture of the following but layout/arrangement is up to the designer.

Happy if the national provider number and abn are on the back, and happy for them to be smaller than the rest.

I am also happy to receive single sided or weird and wonderful designs.

Name
Title
National Provider Number 7192
ABN 53 614 289 117
Level 1, 214 Garrow Street
Elmstead Vale NSW 2291
Ph: 1300 587 902
Mobile: 0438 761 205
name@ironquillbuild.com.au
www.ironquillbuild.com.au

Target Market(s)

Professionals, Peers, Students, Suppliers...

Industry/Entity Type

Construction

Contact Information for Business Card

Listed in project description

Font styles to use
Other font styles liked:
• Century Gothic

Colors
0455a3
3176b5
ffffff

Requirements
Must have
• Professional Design, same color scheme as our logo
Nice to have
• Something that sets our apart from everyone else would be fantastic, open to size and shape and layout options, as long as they present professionally.
• Open to raised/embossed text, alternative materials, custom sizes, clear material
Should not have
• The color orange

```html
<!DOCTYPE html>
<html lang="en">
<head>
<meta charset="utf-8">
<title>Ironquill Build – Business Card</title>
<link rel="stylesheet" href="https://fonts.googleapis.com/css2?family=Open+Sans:wght@400;600;700&display=swap">
<style>
  :root {
    --page-bg: #3a3a3a;
    --card-bg: #141414;
    --card-edge: #1e1e1e;
    --brand-blue: #2b4fa8;
    --name-grey: #8a8a8a;
    --text-light: #e6e6e6;
    --icon-grey: #9a9a9a;
    --divider: #262626;
  }
  * { box-sizing: border-box; margin: 0; padding: 0; }
  html, body { width: 1200px; height: 900px; overflow: hidden; }
  body {
    background: var(--page-bg);
    font-family: "Open Sans", sans-serif;
    display: flex;
    align-items: center;
    justify-content: center;
    gap: 40px;
  }
  .card {
    position: relative;
    width: 520px;
    height: 316px;
    border-radius: 18px;
    background: var(--card-bg);
    border: 1px solid var(--card-edge);
    overflow: hidden;
  }
  /* Front: details side */
  .card-front .brand-panel {
    position: absolute;
    left: 0; top: 0;
    width: 228px; height: 100%;
    border-right: 1px solid var(--divider);
    display: flex;
    align-items: center;
    justify-content: center;
    gap: 10px;
  }
  .brand-mark {
    width: 16px; height: 16px;
    background: var(--brand-blue);
  }
  .brand-name {
    color: var(--brand-blue);
    font-weight: 600;
    font-size: 22px;
    letter-spacing: 0.5px;
  }
  .details {
    position: absolute;
    left: 254px; top: 34px;
    color: var(--text-light);
    font-size: 13px;
    line-height: 1.4;
  }
  .person-name {
    color: var(--name-grey);
    font-weight: 700;
    font-size: 17px;
    line-height: 1.1;
  }
  .person-title { margin-bottom: 14px; }
  .address { margin-bottom: 8px; }
  .contact-list { list-style: none; margin-bottom: 16px; }
  .contact-list li {
    display: flex;
    align-items: center;
    gap: 10px;
    line-height: 1.55;
  }
  .contact-list svg { width: 11px; height: 11px; fill: var(--icon-grey); flex: none; }
  /* Back: brand side */
  .card-back {
    display: flex;
    align-items: center;
    justify-content: center;
    gap: 14px;
  }
  .card-back .brand-mark { width: 26px; height: 26px; }
  .card-back .brand-name { font-size: 40px; font-weight: 400; }
</style>
</head>
<body>
  <section class="card card-front">
    <div class="brand-panel">
      <span class="brand-mark"></span>
      <span class="brand-name">ironquill build</span>
    </div>
    <div class="details">
      <p class="person-name">Daniel Hartley</p>
      <p class="person-title">Managing Director</p>
      <p class="address">Level 1, 214 Garrow Street<br>Elmstead Vale NSW 2291</p>
      <ul class="contact-list">
        <li><svg viewBox="0 0 12 12"><path d="M2.5 0.5l2 2.2-1 1.3c.7 1.5 1.9 2.7 3.4 3.4l1.3-1 2.3 2-1.2 2.1C4.5 10.3 1.6 7.4 0.5 2.7z"/></svg>1300 587 902</li>
        <li><svg viewBox="0 0 12 12"><path d="M3 0h6v12H3zM4 1.5v8h4v-8z"/></svg>0438 761 205</li>
        <li><svg viewBox="0 0 12 12"><path d="M0 2h12v8H0zM1 3l5 3.5L11 3v-.5H1z"/></svg>name@ironquillbuild.com.au</li>
        <li><svg viewBox="0 0 12 12"><circle cx="6" cy="6" r="5.5"/></svg>www.ironquillbuild.com.au</li>
      </ul>
      <p class="provider">National Provider Number 7192<br>ABN 53 614 289 117</p>
    </div>
  </section>

  <section class="card card-back">
    <span class="brand-mark"></span>
    <span class="brand-name">ironquill build</span>
  </section>
</body>
</html>
```